One page responsive Wordpress Website

I am looking to design and code for 1-page Wordpress responsive website (desktop/mobile/tablet). Pls see attached file. Job scope includes Wordpress design and coding of the actual Live website
Target Market(s)
Small medium business
Industry/Entity Type
Telecommunications
Font styles to use
Sans Serif
Colors
ffffff
85cae6
63bae0
33a6d7
cedeed
3277b5
Requirements
Must have
- One page only, Wordpress, Responsive layout in desktop, mobile, tablet

```html
<!DOCTYPE html>
<html lang="en">
<head>
<meta charset="utf-8">
<title>Veltrona IP Phone</title>
<link rel="stylesheet" href="https://fonts.googleapis.com/css2?family=Montserrat:wght@400;500;600;700;800&display=swap">
<style>
:root{
  --white:#ffffff;
  --sky:#85cae6;
  --sky-mid:#63bae0;
  --sky-deep:#33a6d7;
  --mist:#cedeed;
  --brand:#3277b5;
  --brand-dark:#1f5fa3;
  --ink:#1d2b3a;
  --muted:#7b8da1;
}
*{box-sizing:border-box;margin:0;padding:0}
html,body{width:1200px;height:2182px;overflow:hidden}
body{font-family:"Montserrat",sans-serif;color:var(--ink);background:var(--white)}
.page{position:relative;width:1200px;height:2182px;overflow:hidden;background:var(--white)}
.abs{position:absolute}

/* hero */
.hero-bg{left:0;top:0;width:1200px;height:600px;background:linear-gradient(180deg,#2d74b6 0%,#2a86c2 45%,#33a6d7 75%,#2a86c2 100%)}
.hero-map{left:80px;top:130px;width:1040px;height:330px;border-radius:50%;background:radial-gradient(ellipse at center,rgba(133,202,230,.35),rgba(133,202,230,0) 70%)}
.waves{left:0;top:0;width:1200px;height:2182px}
.logo{font-weight:800;color:var(--white);font-size:52px;letter-spacing:-1px;line-height:1}
.site-logo{left:161px;top:24px}
.nav{top:40px;right:161px;display:flex;gap:44px}
.nav a{color:var(--white);text-decoration:none;font-size:14px;font-weight:500}
.hero-kicker{left:0;width:1200px;top:140px;text-align:center;color:var(--white);font-size:22px;font-weight:400}
.hero-title{left:0;width:1200px;top:180px;text-align:center;color:var(--white);font-size:46px;font-weight:800}
.hero-copy{left:0;width:1200px;top:250px;text-align:center;color:var(--white);font-size:14px;line-height:18px;letter-spacing:.3px}

/* product cards */
.card{top:364px;width:277px;height:311px;background:var(--white);border-radius:6px;box-shadow:0 10px 28px rgba(30,70,120,.18);overflow:hidden}
.card h3{text-align:center;color:var(--brand);font-size:22px;font-weight:600;margin-top:24px}
.card .shot{position:absolute;left:78px;top:76px;width:120px;height:126px;border-radius:6px;background:linear-gradient(160deg,#4c5866,#2c3440)}
.card .shot.tall{left:98px;width:80px}
.features{position:absolute;left:0;width:100%;top:220px;display:flex;justify-content:center;gap:7px}
.features span{width:30px;height:30px;border-radius:50%;background:#dbe8f4;border:2px solid #c3d8ec}
.download{position:absolute;left:0;bottom:0;width:100%;height:45px;background:var(--brand);color:var(--white);display:flex;align-items:center;justify-content:center;gap:12px;font-size:14px;font-weight:600}

/* about */
.section-title{color:var(--brand);font-weight:800;font-size:36px}
.about-title{left:161px;top:768px}
.about-copy{left:161px;top:828px;width:480px;font-size:15.5px;line-height:27px}
.about-visual{left:722px;top:778px;width:290px;height:282px;border-radius:8px;background:linear-gradient(160deg,#3e4c5e,#263140)}

/* contact */
.contact-title{left:161px;top:1333px;font-size:35px}
.contact-copy{left:161px;top:1390px;width:410px;font-size:15.5px;line-height:27px}
.contact-copy p+p{margin-top:9px}
.team-visual{left:635px;top:1335px;width:402px;height:206px;border-radius:8px;background:linear-gradient(135deg,#6f95e0,#2a4fc8 60%,#1c2f9c)}
.field{position:absolute;background:var(--white);border:1px solid #d7e3ef;border-radius:2px;font-size:12px;color:var(--muted);padding:10px 10px;font-family:inherit}
.send{left:479px;top:1792px;width:195px;height:44px;background:var(--brand);color:var(--white);font-size:15px;font-weight:600;display:flex;align-items:center;justify-content:center;border-radius:2px}

/* footer */
.footer{left:0;top:1908px;width:1200px;height:274px;background:var(--brand)}
.footer-logo{left:161px;top:1950px;font-size:46px}
.footer-links{left:161px;top:2025px;list-style:none;color:var(--white);font-size:14px}
.footer-links li{display:flex;align-items:center;gap:8px;height:23px}
.footer-links li::before{content:"";width:6px;height:6px;border-radius:50%;border:2.5px solid var(--white);background:var(--brand)}
.footer-heading{left:497px;top:1966px;color:var(--white);font-size:19px;font-weight:600}
.info{display:flex;align-items:flex-start;gap:12px;color:var(--white);font-size:12.5px;line-height:19px}
.info .ico{width:30px;height:30px;flex:none;background:var(--white);border-radius:3px;display:flex;align-items:center;justify-content:center}
.divider{left:161px;top:2137px;width:878px;height:1px;background:rgba(255,255,255,.3)}
.copyright{left:0;width:1200px;top:2153px;text-align:center;color:var(--white);font-size:11.5px}
</style>
</head>
<body>
<div class="page">
  <div class="abs hero-bg"></div>
  <div class="abs hero-map" role="img" aria-label="Faint world map behind the hero heading"></div>

  <svg class="abs waves" viewBox="0 0 1200 2182" aria-hidden="true">
    <path d="M0 474 C 180 540 360 570 600 545 C 820 522 980 475 1200 487 L1200 1203 C 1080 1170 960 1160 820 1190 C 640 1230 470 1270 300 1250 C 170 1235 80 1200 0 1169 Z" fill="#ffffff"/>
    <path d="M0 1169 C 80 1200 170 1235 300 1250 C 470 1270 640 1230 820 1190 C 960 1160 1080 1170 1200 1203 L1200 1908 L0 1908 Z" fill="#cedeed"/>
  </svg>

  <header>
    <div class="abs logo site-logo">Veltrona</div>
    <nav class="abs nav"><a href="#about">About Us</a><a href="#contact">Contact Us</a></nav>
  </header>

  <div class="abs hero-kicker">Enterprise HD IP Phone</div>
  <h1 class="abs hero-title">Veltrona IP Phone</h1>
  <p class="abs hero-copy">The most affordable IP Phone, with highest compatibility to<br>every IP-PBX system. Sleek designed and user-friendly proven.</p>

  <article class="abs card" style="left:161px">
    <h3>Veltrona VT300</h3>
    <div class="shot" role="img" aria-label="Desk IP phone with handset and colour display"></div>
    <div class="features"><span></span><span></span><span></span><span></span></div>
    <div class="download">Download Datasheet (En)
      <svg width="20" height="22" viewBox="0 0 20 22" fill="none" stroke="#fff" stroke-width="1.4"><path d="M3 1h9l4 4v8"/><path d="M3 1v18h7"/><circle cx="14" cy="16" r="5"/><path d="M14 13v6M11.5 16.5 14 19l2.5-2.5"/></svg>
    </div>
  </article>
  <article class="abs card" style="left:461px">
    <h3>Veltrona VT500</h3>
    <div class="shot" role="img" aria-label="Desk IP phone with handset and large colour display"></div>
    <div class="features"><span></span><span></span><span></span><span></span><span></span><span></span></div>
    <div class="download">Download Datasheet (En)
      <svg width="20" height="22" viewBox="0 0 20 22" fill="none" stroke="#fff" stroke-width="1.4"><path d="M3 1h9l4 4v8"/><path d="M3 1v18h7"/><circle cx="14" cy="16" r="5"/><path d="M14 13v6M11.5 16.5 14 19l2.5-2.5"/></svg>
    </div>
  </article>
  <article class="abs card" style="left:761px">
    <h3>Veltrona VX40</h3>
    <div class="shot tall" role="img" aria-label="Expansion module with colour key display"></div>
    <div class="download">Download Datasheet (En)
      <svg width="20" height="22" viewBox="0 0 20 22" fill="none" stroke="#fff" stroke-width="1.4"><path d="M3 1h9l4 4v8"/><path d="M3 1v18h7"/><circle cx="14" cy="16" r="5"/><path d="M14 13v6M11.5 16.5 14 19l2.5-2.5"/></svg>
    </div>
  </article>

  <section id="about">
    <h2 class="abs section-title about-title">About us</h2>
    <p class="abs about-copy">Veltrona IP Phones is designed with pixel colour LCD with backlight LED, built-in Gigabit Ethernet with up to 28 various features. Equipped with Power over Ethernet (PoE) support, and high definition (HD) sound quality with a rich visual experience. Designed with a fresh appearance, it supports flexible and secured provisioning, deliver modern elegant appearance, superb sound quality and a rich set of IP/SIP telephony features.</p>
    <div class="abs about-visual" role="img" aria-label="Desk IP phone set beside an expansion module"></div>
  </section>

  <section id="contact">
    <h2 class="abs section-title contact-title">Contact Us Now</h2>
    <div class="abs contact-copy">
      <p>Speak to us or send us an enquiry for free consultation.</p>
      <p>Our team would love to share more about Veltrona IP Phones. We are expecting your calls and emails. Drop us an enquiry form at your fingertips!</p>
    </div>
    <div class="abs team-visual" role="img" aria-label="Illustration of a team working together around a laptop"></div>

    <div class="field" style="left:161px;top:1622px;width:277px;height:38px">Name</div>
    <div class="field" style="left:461px;top:1622px;width:277px;height:38px">Email Address</div>
    <div class="field" style="left:761px;top:1622px;width:278px;height:38px">Phone Number</div>
    <div class="field" style="left:161px;top:1682px;width:878px;height:86px">Message</div>
    <div class="abs send">Send Message</div>
  </section>

  <footer>
    <div class="abs footer"></div>
    <div class="abs logo footer-logo">Veltrona</div>
    <ul class="abs footer-links"><li>About Us</li><li>Contact Us</li></ul>
    <div class="abs footer-heading">Contact Us</div>

    <div class="abs info" style="left:499px;top:2010px;width:240px">
      <span class="ico"><svg width="18" height="18" viewBox="0 0 18 18" fill="none" stroke="#3277b5" stroke-width="1.3"><path d="M9 15s-4.5-4.5-4.5-8a4.5 4.5 0 0 1 9 0c0 3.5-4.5 8-4.5 8z"/><circle cx="9" cy="7" r="1.7"/><path d="M2 16h14"/></svg></span>
      <span>48 Harbour Lane, #05-12,<br>Singapore 118822</span>
    </div>
    <div class="abs info" style="left:499px;top:2057px;align-items:center">
      <span class="ico"><svg width="18" height="14" viewBox="0 0 18 14" fill="none" stroke="#3277b5" stroke-width="1.3"><rect x="1" y="1" width="16" height="12"/><path d="M1 1l8 7 8-7M1 13l6-6M17 13l-6-6"/></svg></span>
      <span>hello@veltronavoice.example</span>
    </div>
    <div class="abs info" style="left:788px;top:2010px;align-items:center">
      <span class="ico"><svg width="16" height="16" viewBox="0 0 16 16" fill="none" stroke="#3277b5" stroke-width="1.3"><path d="M3 1.5l2.5 0 1.2 3-1.6 1.2a8 8 0 0 0 5.2 5.2l1.2-1.6 3 1.2v2.5a1.5 1.5 0 0 1-1.5 1.5A12.5 12.5 0 0 1 1.5 3 1.5 1.5 0 0 1 3 1.5z"/></svg></span>
      <span>6100-2345</span>
    </div>
    <div class="abs info" style="left:788px;top:2057px">
      <span class="ico"></span>
    </div>

    <div class="abs divider"></div>
    <div class="abs copyright">© Veltrona 2021</div>
  </footer>
</div>
</body>
</html>
```